Hypnosis signage

I need a signage 3.50 mt width x 1.60 length.
I'm attaching a signage.
But few changes the Text in the center slightly out of balance.
I'm attaching also photos that can go in one corner.
Please do keep the color orange

Please I need the signage in Arial Fonts with colors Orange and Black & White for letters or combination
is up to You .

Thank You
Dorian

Colors
f37022

Requirements
Must have
• Clinical Hypnosis
- Weight Loss
- Fear of
Public Speaking
- Anxiety
- Depression
- PTS
- Stop Smoking
- Confidence Building
- Alcohol Moderation

Book now: www.quillbrookvistaway.net
or call 9427 3861
Should not have
• do You guys see the letters on the signage? "Bramwell Pockets" if You can do the that with Weight Loss ,Stop Smoking, Fear Of Public Speaking , Alcohol Moderation . The letters a bit out of balance .

```html
<!DOCTYPE html>
<html lang="en">
<head>
<meta charset="utf-8">
<title>Clinical Hypnosis Signage</title>
<link rel="stylesheet" href="https://fonts.googleapis.com/css2?family=Montserrat:wght@400;500;600;700&display=swap">
<style>
  :root {
    --brand-orange: #f37022;
    --band-orange: #f7901e;
    --ink-black: #000000;
    --paper-white: #ffffff;
    --photo-foliage: #9c8f3e;
    --photo-warm: #d9b48c;
    --photo-light: #efe2cf;
  }
  html, body {
    margin: 0;
    padding: 0;
    width: 1200px;
    height: 548px;
    overflow: hidden;
    background: var(--paper-white);
  }
  .signage {
    position: relative;
    width: 1200px;
    height: 548px;
    overflow: hidden;
    font-family: "Montserrat", Arial, sans-serif;
    background: var(--brand-orange);
  }
  .signage__art {
    position: absolute;
    left: 0;
    top: 0;
    width: 1200px;
    height: 490px;
    display: block;
  }
  .headline {
    position: absolute;
    right: 42px;
    top: 126px;
    margin: 0;
    color: var(--brand-orange);
    font-weight: 600;
    font-size: 66px;
    line-height: 74px;
    text-align: right;
    letter-spacing: 0.5px;
  }
  .services {
    position: absolute;
    top: 308px;
    margin: 0;
    padding: 0;
    list-style: none;
    color: var(--paper-white);
    font-weight: 400;
    font-size: 21px;
    line-height: 41px;
  }
  .services--left { left: 596px; }
  .services--right { left: 892px; }
  .services li::before {
    content: "•";
    margin-right: 4px;
  }
  .booking-band {
    position: absolute;
    left: 0;
    bottom: 0;
    width: 1200px;
    height: 58px;
    background: var(--band-orange);
    color: var(--paper-white);
    font-weight: 600;
    font-size: 30px;
    line-height: 58px;
    padding-left: 37px;
    box-sizing: border-box;
    white-space: nowrap;
  }
</style>
</head>
<body>
  <main class="signage">
    <svg class="signage__art" viewBox="0 0 1200 490" xmlns="http://www.w3.org/2000/svg">
      <defs>
        <linearGradient id="photoFade" x1="0" y1="0" x2="1" y2="0">
          <stop offset="0" stop-color="var(--photo-foliage)" />
          <stop offset="0.2" stop-color="var(--photo-light)" />
          <stop offset="0.45" stop-color="var(--photo-warm)" />
          <stop offset="0.75" stop-color="var(--photo-light)" stop-opacity="0.85" />
          <stop offset="1" stop-color="var(--brand-orange)" stop-opacity="0" />
        </linearGradient>
      </defs>
      <rect class="orange-field" x="0" y="0" width="1200" height="490" fill="var(--brand-orange)" />
      <rect class="couple-photo" x="0" y="0" width="640" height="410" fill="url(#photoFade)"
            role="img" aria-label="Photo of a smiling mature couple embracing outdoors in autumn" />
      <path class="swoosh-white"
            d="M0,345 C250,362 540,285 750,182 C900,105 1050,55 1180,44 L1200,46 L1200,80 C1100,86 950,122 800,202 C600,302 300,402 0,392 Z"
            fill="var(--paper-white)" />
      <path class="panel-black"
            d="M0,392 C300,402 600,302 800,202 C950,122 1100,86 1200,80 L1200,490 L0,490 Z"
            fill="var(--ink-black)" />
    </svg>

    <h1 class="headline">Clinical<br>Hypnosis</h1>

    <ul class="services services--left">
      <li>Weight Loss</li>
      <li>Fear of Public Speaking</li>
      <li>Anxiety</li>
      <li>Depression</li>
    </ul>
    <ul class="services services--right">
      <li>PTS</li>
      <li>Stop Smoking</li>
      <li>Confidence Building</li>
      <li>Alcohol Moderation</li>
    </ul>

    <div class="booking-band">Book now : www.quillbrookvistaway.net | or call 9427 3861</div>
  </main>
</body>
</html>
```